tovrin company need business card, envelope and letterhead design

Check on the attached file wherein you can find our logo and information about the company
Business card will double sided English version and Arabic version

Industry/Entity Type

Business

Requirements
Must have
• include the design also for the letterhead and envelop
Nice to have

```html
<!DOCTYPE html>
<html lang="en">
<head>
<meta charset="utf-8">
<title>Tovrin Business Card</title>
<link rel="stylesheet" href="https://fonts.googleapis.com/css2?family=Roboto:wght@400;500;700&family=Michroma&display=swap">
<style>
  :root {
    --brand-blue: #1271b8;
    --brand-blue-line: #1a6fc2;
    --panel-grey: #8d8e90;
    --panel-grey-light: #a3a4a6;
    --card-white: #f7f7f7;
    --page-bg: #e4e5e7;
    --ink-white: #ffffff;
  }
  * { box-sizing: border-box; margin: 0; padding: 0; }
  html, body { width: 1200px; height: 886px; overflow: hidden; }
  body {
    background: var(--page-bg);
    font-family: "Roboto", Arial, sans-serif;
    display: flex;
    flex-direction: column;
    align-items: center;
    justify-content: center;
    gap: 56px;
  }
  .card {
    position: relative;
    width: 620px;
    height: 354px;
    box-shadow: 0 6px 18px rgba(0,0,0,0.18);
    overflow: hidden;
  }
  .card--front { background: var(--brand-blue); }
  .card--back { background: var(--card-white); }

  .brand {
    display: flex;
    align-items: center;
    gap: 14px;
  }
  .brand__mark { width: 40px; height: 40px; }
  .brand__name {
    font-family: "Michroma", "Roboto", sans-serif;
    font-weight: 400;
    letter-spacing: 2px;
  }
  .card--front .brand {
    position: absolute;
    left: 50%; top: 138px;
    transform: translateX(-50%);
  }
  .card--front .brand__mark { background: var(--ink-white); }
  .card--front .brand__name { color: var(--ink-white); font-size: 44px; }
  .front__url {
    position: absolute;
    left: 0; right: 0; top: 258px;
    text-align: center;
    color: var(--ink-white);
    font-size: 13px;
    letter-spacing: 9px;
  }

  .card--back .brand {
    position: absolute;
    left: 50px; top: 160px;
  }
  .card--back .brand__mark { width: 30px; height: 30px; background: var(--brand-blue); }
  .card--back .brand__name { color: var(--brand-blue); font-size: 30px; }

  .panel { position: absolute; inset: 0; width: 620px; height: 354px; }
  .contact {
    position: absolute;
    left: 330px; top: 42px;
    color: var(--ink-white);
    font-size: 12.5px;
    line-height: 1.32;
  }
  .contact__name { font-size: 17px; font-weight: 700; }
  .contact__role { font-size: 14px; font-weight: 500; margin-bottom: 2px; }
  .contact__address { margin-top: 10px; }
  .contact__list { list-style: none; margin-top: 10px; }
  .contact__list li { display: flex; align-items: center; gap: 8px; }
  .contact__list svg { width: 12px; height: 12px; fill: var(--ink-white); flex: none; }
</style>
</head>
<body>

<section class="card card--front" aria-label="Business card front">
  <div class="brand">
    <span class="brand__mark"></span>
    <span class="brand__name">TOVRIN</span>
  </div>
  <p class="front__url">www.tovrin.com</p>
</section>

<section class="card card--back" aria-label="Business card back">
  <svg class="panel" viewBox="0 0 620 354" aria-hidden="true">
    <defs>
      <linearGradient id="panelShade" x1="0" y1="0" x2="1" y2="1">
        <stop offset="0" stop-color="#8a8b8d"/>
        <stop offset="1" stop-color="#a7a8aa"/>
      </linearGradient>
    </defs>
    <polygon points="345,0 620,0 620,292 392,322 272,162" fill="url(#panelShade)"/>
    <polyline points="332,-2 258,162 384,336 620,300" fill="none" stroke="var(--brand-blue-line)" stroke-width="4"/>
  </svg>

  <div class="brand">
    <span class="brand__mark"></span>
    <span class="brand__name">TOVRIN</span>
  </div>

  <div class="contact">
    <p class="contact__name">Faris Bin Omar Al Hamdan</p>
    <p class="contact__role">General Manager</p>
    <p>+966 555 010 234</p>
    <p class="contact__address">Qasr Garden Road<br>Al Noor District-P.O. Box 4410-11220<br>Kingdom of Saudi Arabia</p>
    <ul class="contact__list">
      <li><svg viewBox="0 0 24 24"><path d="M6.6 10.8a15.1 15.1 0 0 0 6.6 6.6l2.2-2.2a1 1 0 0 1 1-.25 11.4 11.4 0 0 0 3.6.57 1 1 0 0 1 1 1V20a1 1 0 0 1-1 1A17 17 0 0 1 3 4a1 1 0 0 1 1-1h3.5a1 1 0 0 1 1 1c0 1.25.2 2.45.57 3.57a1 1 0 0 1-.25 1z"/></svg>011 0102 345</li>
      <li><svg viewBox="0 0 24 24"><path d="M6 2h12v6H6zM4 9h16a2 2 0 0 1 2 2v7h-4v4H6v-4H2v-7a2 2 0 0 1 2-2zm4 7v4h8v-4z"/></svg>011 0102 346</li>
      <li><svg viewBox="0 0 24 24"><path d="M2 5h20v14H2zm2 2v.5l8 5 8-5V7zm0 3v7h16v-7l-8 5z"/></svg>tovrin.sa@mailbox.com</li>
      <li><svg viewBox="0 0 24 24"><path d="M12 2a10 10 0 1 0 0 20 10 10 0 0 0 0-20zm0 2c.9 1.2 1.6 2.6 2 4h-4c.4-1.4 1.1-2.8 2-4zM4.3 14a8 8 0 0 1 0-4h3.4a16 16 0 0 0 0 4zm5.4 0a14 14 0 0 1 0-4h4.6a14 14 0 0 1 0 4zm6.6 0a16 16 0 0 0 0-4h3.4a8 8 0 0 1 0 4zM12 20c-.9-1.2-1.6-2.6-2-4h4c-.4 1.4-1.1 2.8-2 4z"/></svg>www.tovrin.com</li>
    </ul>
  </div>
</section>

</body>
</html>
```